Redesign of Grown Collector of BRIXO Weblog.

I'm an Grown Collector of BRIXO (GCOB), and I'm the person behind a small, off-the-beaten-path fan site, built using WordPress.

The existing site is at http://quietfern.example. As you can see, it could use an infinitely better design!

My site was originally for reviews of BRIXO sets, and had extended to include general commentary and a small gallery of models I've built and a cast of characters. It's particularly known for my opinions and perspective on the world of BRIXO, and as such isn't necessarily child friendly.
While keeping existing content, the new version of the site will focus more on video content from my VidNook channel.

In contrast to the current site, I'm looking for a light design that makes use of a few muted, low saturation colours, whilst remaining clean and relatively simple. The logo is part of the site's identity and should serve as inspiration for the design.
The content pages would keep the thin floating menu, and the content area would be no more than 1200 pixels wide.
Though it's a BRIXO fan site, I would like to avoid overt references to BRIXO elements. Other that that, you're more than welcome to use your creative license with the design.

In addition to the home, blog and post pages, I would also like a "placeholder" page that can be adapted for different page types. I will be building the theme from the designs, so don't worry about doing any coding.
You don't have to provide them all at once at this stage: I would suggest submitting either the home page or post page.

The final design should communicate "this is MY corner of the web", but above all else that it's about creativity and self-expression.

If you have any questions, please get in touch!
Updates

Target Market(s)

People interested in BRIXO in general, 12 and up.

Industry/Entity Type

Adult

Number of Pages Required

4 page

Font styles to use
Sans Serif
Decorative
Other font styles liked:
• Qhytsdakx

Requirements
Must have
• The tagline "Do Your Thing".
• I'm keeping the font/fount used for headings (Qhytsdakx); I'm open to suggestions for the body text.
Should not have
• Overt references to BRIXO or BRIXO elements.

```html
<!DOCTYPE html>
<html lang="en">
<head>
<meta charset="utf-8">
<title>QuietFern — Do Your Thing</title>
<link rel="stylesheet" href="https://fonts.googleapis.com/css2?family=Teko:wght@400;500&family=Roboto+Condensed:wght@700&family=Open+Sans:ital,wght@0,400;0,600;0,700;1,400&display=swap">
<style>
:root{
  --ink:#222;
  --ink-soft:#555;
  --muted:#777;
  --rule:#888;
  --hero-hi:#ececec;
  --hero-lo:#d2d2d2;
  --paper:#fff;
  --band:#ececec;
  --tile:#6f6f6f;
  --dark:#222;
  --dark-2:#2b2b2b;
  --btn:#222;
  --btn-edge:#777;
  --white:#fff;
}
*{box-sizing:border-box;margin:0;padding:0}
html,body{width:1200px;height:2296px;overflow:hidden}
body{font-family:"Open Sans",sans-serif;color:var(--ink);background:var(--paper);position:relative}
.heading{font-family:"Teko",sans-serif;font-weight:400;text-transform:uppercase;letter-spacing:.5px;color:var(--ink);line-height:1}
.btn{display:inline-flex;align-items:center;height:37px;padding:0 18px;background:var(--btn);color:var(--white);font-size:11px;font-weight:600;text-transform:uppercase;border-right:5px solid var(--btn-edge);box-shadow:3px 0 0 var(--paper)}
.more{font-size:11px;font-weight:600;text-transform:uppercase;border-left:2px solid var(--ink);padding-left:4px;line-height:1}
.media{display:block;border:1px solid #ddd}

/* hero */
.hero{position:absolute;top:0;left:0;width:1200px;height:577px;background:radial-gradient(ellipse at 50% 40%,var(--hero-hi),var(--hero-lo));box-shadow:inset 0 -30px 40px -20px rgba(0,0,0,.12)}
.hero .btn{box-shadow:3px 0 0 var(--hero-hi)}
.brand{position:absolute;left:161px;top:44px;display:flex;align-items:center;gap:12px;color:var(--ink);font-weight:700;font-size:30px;line-height:1;letter-spacing:-.5px}
.brand-mark{width:18px;height:18px;background:var(--dark)}
.phone{position:absolute;left:905px;top:20px;display:flex;gap:12px;align-items:center}
.phone small{display:block;font-size:11px;color:var(--muted)}
.phone b{font-weight:400;font-size:14px;color:var(--ink-soft)}
.nav{position:absolute;right:163px;top:80px;display:flex;gap:28px;font-size:13px;font-weight:600;text-transform:uppercase;color:var(--ink)}
.hero-copy{position:absolute;left:161px;top:212px;width:340px}
.hero-copy h1{font-size:36px}
.hero-copy .lead{font-family:"Roboto Condensed",sans-serif;font-size:13px;line-height:17px;margin-top:20px;color:var(--ink)}
.hero-copy p{font-size:11.5px;line-height:17px;color:var(--ink-soft);margin-top:14px}
.hero-copy .btn{margin-top:24px}
.player{position:absolute;left:555px;top:177px;width:480px;height:313px;background:#111}
.player .screen{position:absolute;inset:18px 0 28px 0;background:linear-gradient(135deg,#b9b4c4,#8e97a6 50%,#6f7c8a)}
.player .play{position:absolute;left:210px;top:130px;width:62px;height:46px;background:rgba(20,20,20,.85)}
.player .bar{position:absolute;left:0;right:0;bottom:0;height:28px;background:#1b1b1b;color:#aaa;font-size:10px;display:flex;align-items:center;justify-content:flex-end;padding-right:50px}
.arrow{position:absolute;top:310px;width:48px;height:48px;border-radius:50%;background:#a9a9a9}

/* section heads */
.sec-head{position:absolute;border-left:3px solid var(--rule);padding-left:10px}
.sec-head h2{font-size:30px}
.sec-head em{display:block;font-size:12px;color:var(--muted);margin-top:4px}
.pager{position:absolute}

/* cards */
.card{position:absolute;width:270px}
.card h3{font-size:12px;font-weight:700;text-transform:uppercase;margin-top:22px}
.card p{font-size:11px;line-height:17px;color:var(--ink-soft);margin-top:10px}

.reviews{position:absolute;top:980px;left:0;width:1200px;height:413px;background:var(--band);border-top:1px solid #ddd;border-bottom:1px solid #ddd}
.feature{position:absolute;left:161px;top:78px;width:511px;height:287px;background:linear-gradient(160deg,#e6e3a8,#b9b88a 45%,#6a5a50)}
.feature .cap{position:absolute;left:0;right:0;bottom:0;height:90px;background:rgba(40,40,40,.82);color:#eee;padding:14px 22px;font-size:11.5px;line-height:17px}
.date{font-size:11px;display:flex;gap:6px;align-items:center;margin-bottom:9px}
.mini{position:absolute;left:713px;width:324px;height:91px;display:flex;background:var(--tile)}
.mini .thumb{width:95px;background:linear-gradient(135deg,#bbb,#777)}
.mini .txt{padding:8px 10px;color:#eee;font-size:10.5px;line-height:15px}
.mini .date{margin-bottom:4px}

/* footer */
.foot{position:absolute;top:1844px;left:0;width:1200px;height:314px;background:linear-gradient(120deg,#2d3a2c,#262626 30%,#2c2624 70%,#3a2e2a)}
.foot h4{font-family:"Teko",sans-serif;font-weight:400;font-size:27px;color:var(--white)}
.grid{display:grid;grid-template-columns:repeat(4,99px);gap:5px;margin-top:16px}
.grid span{height:87px;background:linear-gradient(135deg,#8a8a8a,#4f4f4f)}
.tweet{display:flex;gap:14px;font-size:10.5px;line-height:16px;color:#ddd;padding:12px 0;border-bottom:1px solid #777}
.tweet:last-child{border:0}
.tweet i{flex:none;width:12px;height:12px;background:#ddd;margin-top:2px}
.base{position:absolute;top:2158px;left:0;width:1200px;height:138px;background:var(--dark-2);text-align:center;color:#ddd}
.social{display:flex;gap:6px;justify-content:center;margin-top:25px}
.social i{width:30px;height:30px;border-radius:50%;border:2px solid #fff}
.links{font-size:10.5px;margin-top:18px;text-transform:uppercase;word-spacing:2px}
.copy{font-size:10.5px;margin-top:10px}
</style>
</head>
<body>

<header class="hero">
  <div class="brand"><span class="brand-mark"></span><span>quietfern.tv</span></div>
  <div class="phone">
    <svg width="26" height="26" viewBox="0 0 26 26"><circle cx="13" cy="13" r="11.5" fill="none" stroke="#555" stroke-width="1.5"/><path d="M9 8c1-1 2 0 2.5 1.2l-1 1.3c.8 1.8 2 3 3.8 3.8l1.3-1c1.2.5 2.2 1.5 1.2 2.5-1.5 1.6-4 .3-5.7-1.4S7.4 9.6 9 8z" fill="#555"/></svg>
    <div><small>Phone:</small><b>(888) 555-0142</b></div>
  </div>
  <nav class="nav"><span>Commentary</span><span>Reviews</span><span>MOCs</span><span>Cast</span><span>About</span><span>Contact</span></nav>

  <div class="arrow" style="left:37px"><svg width="48" height="48"><path d="M27 18l-6 6 6 6" fill="none" stroke="#fff" stroke-width="2"/></svg></div>
  <div class="arrow" style="left:1101px"><svg width="48" height="48"><path d="M21 18l6 6-6 6" fill="none" stroke="#fff" stroke-width="2"/></svg></div>

  <div class="hero-copy">
    <h1 class="heading">Welcome to QuietFern</h1>
    <p class="lead">Sed ut perspiciatis unde omnis iste natus error sit voluptatem acium doloremque laudantium, totam rem aperiam, eaque ipsa quae.</p>
    <p>Sed ut perspiciatis unde omnis iste natus error sit volup tatem accusantium doloremque laudantium, totam rem ap er iam, eaque ipsa quae ab illo inventore veritatis et quasi archit ecto beatae vitae dicta sunt explicabo.</p>
    <span class="btn">Read more »</span>
  </div>

  <div class="player">
    <div class="screen" role="img" aria-label="Video still of toy figures in a shop scene"></div>
    <svg class="play" viewBox="0 0 62 46"><path d="M24 13l16 10-16 10z" fill="#fff"/></svg>
    <div class="bar">VidNook</div>
  </div>
</header>

<section>
  <div class="sec-head" style="left:161px;top:600px"><h2 class="heading">Commentary</h2><em>We give you our thoughts, opinions, rants and coverage on the world of BRIXO</em></div>
  <svg class="pager" style="left:1005px;top:600px" width="34" height="20"><path d="M11 3L4 10l7 7M23 3l7 7-7 7" fill="none" stroke="#888" stroke-width="2"/></svg>
  <article class="card" style="left:161px;top:673px"><div class="media" role="img" aria-label="Toy garden stall with fountain" style="height:139px;background:linear-gradient(135deg,#c9b5cf,#8ea08a 50%,#d9d9e2)"></div><h3>Harwick windows at Blockfest 2015</h3><p>Sed ut perspiciatis unde omnis iste natus error sit volu ptatem accusantium doloremque laudantium, totam rem aperiam, eaque ipsa quae ab illo inve.</p><div class="more" style="margin-top:18px">Read more »</div></article>
  <article class="card" style="left:464px;top:673px"><div class="media" role="img" aria-label="Toy wedding couple figures" style="height:139px;background:linear-gradient(135deg,#f3f3ec,#dcd8b8 50%,#f4f4f4)"></div><h3>Harwick windows at Blockfest 2015</h3><p>Sed ut perspiciatis unde omnis iste natus error sit volu ptatem accusantium doloremque laudantium, totam rem aperiam, eaque ipsa quae ab illo inve.</p><div class="more" style="margin-top:18px">Read more »</div></article>
  <article class="card" style="left:767px;top:673px"><div class="media" role="img" aria-label="Three toy figures in swimwear" style="height:139px;background:linear-gradient(90deg,#d8c9a0,#c8b079 50%,#d6d3cb)"></div><h3>Harwick windows at Blockfest 2015</h3><p>Sed ut perspiciatis unde omnis iste natus error sit volu ptatem accusantium doloremque laudantium, totam rem aperiam, eaque ipsa quae ab illo inve.</p><div class="more" style="margin-top:18px">Read more »</div></article>
</section>

<section class="reviews">
  <div class="sec-head" style="left:161px;top:32px"><h2 class="heading">Reviews</h2></div>
  <div class="feature" role="img" aria-label="Toy living room set with figures">
    <div class="cap"><div class="date"><svg width="11" height="11" viewBox="0 0 11 11"><rect x=".5" y="1.5" width="10" height="9" fill="none" stroke="#eee"/><path d="M.5 4h10M3 0v3M8 0v3" stroke="#eee"/></svg>FEB 15, 2016</div>Sed ut perspiciatis unde omnis iste natus error sit voluptatem accusantium dolore mue laudantium, totam rem Sed ut perspiciatis unde omnis iste natus</div>
  </div>
  <div class="mini" style="top:77px"><div class="thumb" role="img" aria-label="Toy forest scene"></div><div class="txt"><div class="date"><svg width="11" height="11" viewBox="0 0 11 11"><rect x=".5" y="1.5" width="10" height="9" fill="none" stroke="#eee"/><path d="M.5 4h10M3 0v3M8 0v3" stroke="#eee"/></svg>FEB 15, 2016</div>Sed ut perspiciatis unde omnis iste natus error sit voluptatem accusantium dolore mque laudantium, totam rem</div></div>
  <div class="mini" style="top:176px"><div class="thumb" role="img" aria-label="Toy figure portrait"></div><div class="txt"><div class="date"><svg width="11" height="11" viewBox="0 0 11 11"><rect x=".5" y="1.5" width="10" height="9" fill="none" stroke="#eee"/><path d="M.5 4h10M3 0v3M8 0v3" stroke="#eee"/></svg>FEB 15, 2016</div>Sed ut perspiciatis unde omnis iste natus error sit voluptatem accusantium dolore mque laudantium, totam rem</div></div>
  <div class="mini" style="top:275px"><div class="thumb" role="img" aria-label="Toy vehicle"></div><div class="txt"><div class="date"><svg width="11" height="11" viewBox="0 0 11 11"><rect x=".5" y="1.5" width="10" height="9" fill="none" stroke="#eee"/><path d="M.5 4h10M3 0v3M8 0v3" stroke="#eee"/></svg>FEB 15, 2016</div>Sed ut perspiciatis unde omnis iste natus error sit voluptatem accusantium dolore mque laudantium, totam rem</div></div>
</section>

<section>
  <div class="sec-head" style="left:161px;top:1430px"><h2 class="heading">MOCs</h2><em>Short for My Own Creations</em></div>
  <svg class="pager" style="left:400px;top:1437px" width="34" height="20"><path d="M11 3L4 10l7 7M23 3l7 7-7 7" fill="none" stroke="#888" stroke-width="2"/></svg>
  <div class="sec-head" style="left:464px;top:1430px"><h2 class="heading">Features</h2><em>Short for My Own Creations</em></div>
  <svg class="pager" style="left:702px;top:1437px" width="34" height="20"><path d="M11 3L4 10l7 7M23 3l7 7-7 7" fill="none" stroke="#888" stroke-width="2"/></svg>
  <div class="sec-head" style="left:767px;top:1430px"><h2 class="heading">Cast</h2><em>Short for My Own Creations</em></div>
  <svg class="pager" style="left:1005px;top:1437px" width="34" height="20"><path d="M11 3L4 10l7 7M23 3l7 7-7 7" fill="none" stroke="#888" stroke-width="2"/></svg>

  <article class="card" style="left:161px;top:1502px"><div class="media" role="img" aria-label="Toy figures at a shop counter" style="height:147px;background:linear-gradient(135deg,#c6c2b8,#8d7a6e 60%,#6b5448)"></div><h3>Harwick windows at Blockfest 2015</h3><p>Sed ut perspiciatis unde omnis iste natus error sit volu ptatem accusantium doloremque laudantium, totam rem aperiam, eaque ipsa quae ab illo inve.</p><span class="btn" style="margin-top:14px">Read more »</span></article>
  <article class="card" style="left:464px;top:1502px"><div class="media" role="img" aria-label="Group of suited toy figures" style="height:147px;background:linear-gradient(135deg,#c9ccd6,#55504e 55%,#2a2a2e)"></div><h3>Harwick windows at Blockfest 2015</h3><p>Sed ut perspiciatis unde omnis iste natus error sit volu ptatem accusantium doloremque laudantium, totam rem aperiam, eaque ipsa quae ab illo inve.</p><span class="btn" style="margin-top:14px">Read more »</span></article>
  <article class="card" style="left:767px;top:1502px"><div class="media" role="img" aria-label="Toy figure in bee costume" style="height:147px;background:radial-gradient(circle at 50% 50%,#e8b23a,#f07a2c 60%,#f26a22)"></div><h3>Harwick windows at Blockfest 2015</h3><p>Sed ut perspiciatis unde omnis iste natus error sit volu ptatem accusantium doloremque laudantium, totam rem aperiam, eaque ipsa quae ab illo inve.</p><span class="btn" style="margin-top:14px">Read more »</span></article>
</section>

<footer class="foot" role="img" aria-label="Dark blurred backdrop of toy figures">
  <div style="position:absolute;left:161px;top:36px">
    <h4>Snapfold Photostream</h4>
    <div class="grid"><span></span><span></span><span></span><span></span><span></span><span></span><span></span><span></span></div>
  </div>
  <div style="position:absolute;left:597px;top:30px;width:1px;height:260px;background:#666"></div>
  <div style="position:absolute;left:636px;top:36px;width:390px">
    <h4>@QuietFern1</h4>
    <div style="margin-top:10px">
      <div class="tweet"><i></i><div>Phasellus porta. Fusce susct varius mi. Cum sociis natoque penabus et magnis dis parturient montes, nascetur ridiculus mus.<br>http://qf.example/j8Nwnt6</div></div>
      <div class="tweet"><i></i><div>Phasellus porta. Fusce susct varius mi. Cum sociis natoque penabus et magnis dis parturient montes, nascetur ridiculus mus.<br>http://qf.example/j8Nwnt6</div></div>
      <div class="tweet"><i></i><div>Phasellus porta. Fusce susct varius mi. Cum sociis natoque penabus et magnis dis parturient montes, nascetur ridiculus mus.<br>http://qf.example/j8Nwnt6</div></div>
    </div>
  </div>
</footer>

<div class="base">
  <div class="social"><i style="background:#4aa3df"></i><i style="background:#3b5a9a"></i><i style="background:#2a78b0"></i><i style="background:#d2493a"></i></div>
  <div class="links">About us &nbsp;/&nbsp; Commentary &nbsp;/&nbsp; Reviews &nbsp;/&nbsp; MOCs &nbsp;/&nbsp; Cast &nbsp;/&nbsp; Contact us</div>
  <div class="copy">2016 © Copyrights QuietFern.All Rights Reserved</div>
</div>

</body>
</html>
```